Tallowbrook Fitness - Personal & Rehab Training

Business Card for my personal training business - Tallowbrook Fitness. I focus on personal and rehab training. I would like a double sided card, round edges. front of card will be my existing logo and the back will have an image (black and white or exercise, people exercising, weights, etc) along with my name and details. Such as:
Corisse Pembly
Personal & Rehab Trainer
www.tallowbrookfitness.com.au
0438264905
I have some images that I have downloaded that I am happy to send to the designer.
Thanks
Target Market(s)
athletes, middle to high income, sport related
Contact Information for Business Card
Corisse Pembly
Personal & Rehab Trainer
0438264905
Colors
Designer to choose only greyscale colors for use in the design.
Requirements
Must have
- my existing logo
Nice to have
- one of the images uploaded. I really like the girl with the mint coloured shoes as this is one of my logo colours

```html
<!DOCTYPE html>
<html lang="en">
<head>
<meta charset="utf-8">
<title>Tallowbrook Fitness – Business Card</title>
<link rel="stylesheet" href="https://fonts.googleapis.com/css2?family=Lato:wght@400;700&display=swap">
<style>
  :root {
    --bg: #2a2a2b;
    --card: #0e0e0f;
    --card-edge: #1c1c1d;
    --white: #f2f2f2;
    --grey: #bdbdbd;
    --rule: #6a6a6a;
    --mint: #9fe0b8;
    --photo-dark: #1b1b1b;
    --photo-light: #8a8a8a;
  }
  * { box-sizing: border-box; margin: 0; padding: 0; }
  html, body { width: 1200px; height: 900px; overflow: hidden; }
  body {
    background: var(--bg);
    font-family: "Lato", Arial, sans-serif;
    display: flex;
    flex-direction: column;
    align-items: center;
    justify-content: center;
    gap: 40px;
  }
  .card {
    position: relative;
    width: 660px;
    height: 377px;
    border-radius: 26px;
    background: var(--card);
    box-shadow: 0 0 0 1px var(--card-edge), 0 18px 40px rgba(0,0,0,.45);
    overflow: hidden;
  }
  .brand-name {
    font-weight: 400;
    color: var(--white);
    letter-spacing: 0.14em;
    text-transform: uppercase;
    white-space: nowrap;
  }
  /* Logo side */
  .card-front .brand-name {
    position: absolute;
    left: 50%;
    top: 50%;
    transform: translate(-50%, -50%);
    font-size: 28px;
  }
  /* Details side */
  .card-back .photo {
    position: absolute;
    left: 50px;
    top: 140px;
    width: 290px;
    height: 197px;
    border-radius: 6px 14px 14px 6px;
    background: linear-gradient(120deg, var(--photo-dark) 0%, var(--photo-light) 55%, #3a3a3a 100%);
  }
  .card-back .brand-name {
    position: absolute;
    right: 40px;
    top: 72px;
    font-size: 19px;
    letter-spacing: 0.12em;
  }
  .details {
    position: absolute;
    left: 370px;
    top: 150px;
    width: 260px;
  }
  .person-name {
    font-weight: 700;
    font-size: 21px;
    color: var(--mint);
    text-transform: uppercase;
    letter-spacing: 0.01em;
    white-space: nowrap;
  }
  .person-role {
    font-size: 14px;
    color: var(--grey);
    text-transform: uppercase;
    margin-top: 2px;
    white-space: nowrap;
  }
  .divider {
    height: 1px;
    background: var(--rule);
    margin: 16px 0 20px;
    width: 250px;
  }
  .contact {
    font-size: 14px;
    color: var(--grey);
    line-height: 1.35;
    text-transform: uppercase;
    white-space: nowrap;
  }
</style>
</head>
<body>
  <section class="card card-front" aria-label="Business card logo side">
    <p class="brand-name">Tallowbrook Fitness</p>
  </section>

  <section class="card card-back" aria-label="Business card details side">
    <div class="photo" role="img" aria-label="Black and white photo of an athlete training with a battle rope"></div>
    <p class="brand-name">Tallowbrook Fitness</p>
    <div class="details">
      <p class="person-name">Corisse Pembly</p>
      <p class="person-role">Personal &amp; Rehab Trainer</p>
      <div class="divider"></div>
      <p class="contact">0438264905</p>
      <p class="contact">www.tallowbrookfitness.com.au</p>
    </div>
  </section>
</body>
</html>
```